Cutting Board Oil and Finish

I designed these two labels and I am now wanting something a little more professional looking. The label should catch your eye, be unique but also professional. The design can also play off some of the ingredients too if you think that might look good ( beeswax, lemon oil, orange oil) I need two labels: One will be for the bottle of oil and the other will be for the bottle of finish. They are both the same brand so both labels should have the same theme and look related. The dimensions of the label for the bottle of oil will be 4 x 2.25 inches. The dimensions for the bottle of finish will be 3 x 2.125 inches
Target Market(s)
Anyone who uses cutting boards: moms, dads, chefs, woodworkers etc
Industry/Entity Type
It Professional
Look and feel

```html
<!DOCTYPE html>
<html lang="en">
<head>
<meta charset="utf-8">
<title>Holland's Cutting Board Labels</title>
<link rel="stylesheet" href="https://fonts.googleapis.com/css2?family=Antonio:wght@400;500;600;700&family=Open+Sans:wght@400&display=swap">
<style>
  :root {
    --forest: #03553d;
    --gold: #daa520;
    --paper: #ffffff;
    --ink: #111111;
    --citrus-orange: #f07a1a;
    --citrus-yellow: #f5c81c;
    --wood-dark: #7a0d0a;
    --wood-light: #f09a5a;
  }
  * { margin: 0; padding: 0; box-sizing: border-box; }
  html, body { width: 1200px; height: 1000px; overflow: hidden; background: var(--paper); }
  .canvas { position: relative; width: 1200px; height: 1000px; }

  .label {
    position: absolute;
    background: var(--paper);
    box-shadow: 0 4px 14px rgba(0,0,0,0.45);
    overflow: hidden;
  }
  .label-oil { left: 157px; top: 212px; width: 357px; height: 571px; }
  .label-finish { left: 632px; top: 355px; width: 415px; height: 293px; }

  .label-field { position: absolute; left: 0; top: 0; }

  .brand-name, .product-title, .tagline, .ingredients {
    position: absolute; left: 0; width: 100%; text-align: center;
    color: var(--paper); font-family: "Antonio", sans-serif;
    white-space: nowrap; line-height: 1;
  }
  .brand-name { font-weight: 700; letter-spacing: 0.5px; }
  .product-title { font-weight: 700; letter-spacing: 0.2px; }
  .tagline { font-weight: 600; }
  .ingredients { font-weight: 600; }
  .volume {
    position: absolute; left: 0; width: 100%; text-align: center;
    font-family: "Open Sans", sans-serif; color: var(--ink);
    white-space: nowrap; line-height: 1;
  }

  .gold-band { position: absolute; left: 0; width: 100%; background: var(--gold); }

  .citrus-art {
    position: absolute; border-radius: 40px;
    background: linear-gradient(90deg, var(--citrus-orange), #f4a31c 50%, var(--citrus-yellow));
  }
  .honey-art {
    position: absolute; border-radius: 12px;
    background: linear-gradient(90deg, #f4c21a, #f8d440);
  }
  .wood-drop-art {
    position: absolute; border-radius: 50%;
    border: 3px solid var(--gold);
    background: linear-gradient(90deg, var(--wood-dark), var(--wood-light) 35%, #f6b07a 55%, var(--wood-light) 70%, var(--wood-dark));
  }

  /* oil label */
  .label-oil .brand-name { top: 84px; font-size: 28px; }
  .label-oil .product-title { top: 166px; font-size: 50px; }
  .label-oil .tagline { top: 225px; font-size: 13px; letter-spacing: 3.6px; }
  .label-oil .gold-band { top: 370px; height: 28px; }
  .label-oil .citrus-art { left: 90px; top: 318px; width: 180px; height: 52px; }
  .label-oil .wood-drop-art { left: 121px; top: 326px; width: 114px; height: 114px; }
  .label-oil .ingredients { top: 505px; font-size: 15px; }
  .label-oil .volume { top: 551px; font-size: 14px; }

  /* finish label */
  .label-finish .brand-name { top: 42px; font-size: 20px; }
  .label-finish .product-title { top: 77px; font-size: 40px; }
  .label-finish .tagline { top: 119px; font-size: 10px; }
  .label-finish .gold-band { top: 173px; height: 22px; }
  .label-finish .citrus-art { left: 138px; top: 138px; width: 138px; height: 36px; }
  .label-finish .honey-art { left: 138px; top: 195px; width: 138px; height: 30px; }
  .label-finish .wood-drop-art { left: 165px; top: 142px; width: 86px; height: 86px; }
  .label-finish .ingredients { top: 235px; font-size: 11px; }
  .label-finish .volume { top: 274px; font-size: 13px; }
</style>
</head>
<body>
<div class="canvas">

  <section class="label label-oil">
    <svg class="label-field" width="357" height="571" viewBox="0 0 357 571">
      <path fill="var(--forest)" d="M0 49 H76 Q84 49 92 42 C130 12 227 12 265 42 Q273 49 281 49 H357 V538 H0 Z"/>
      <path fill="none" stroke="var(--gold)" stroke-width="4" d="M0 56 H79 Q88 56 96 49 C132 22 225 22 261 49 Q269 56 278 56 H357"/>
      <rect x="0" y="532" width="357" height="5" fill="var(--gold)"/>
    </svg>
    <div class="brand-name">HOLLAND'S</div>
    <h1 class="product-title">CUTTING BOARD OIL</h1>
    <div class="tagline">ALL NATURAL AND FOOD- SAFE</div>
    <div class="citrus-art" role="img" aria-label="Orange and lemon slices illustration"></div>
    <div class="gold-band"></div>
    <div class="wood-drop-art" role="img" aria-label="Wood grain circle with oil drops illustration"></div>
    <div class="ingredients">Food-Grade Mineral oil enriched with Orange oil and Lemon oil</div>
    <div class="volume">8FL OZ</div>
  </section>

  <section class="label label-finish">
    <svg class="label-field" width="415" height="293" viewBox="0 0 415 293">
      <path fill="var(--forest)" d="M0 43 H82 Q90 43 98 36 C145 2 285 2 320 36 Q328 43 336 43 H415 V266 H0 Z"/>
      <path fill="none" stroke="var(--gold)" stroke-width="4" d="M0 51 H85 Q93 51 101 44 C148 14 282 14 317 44 Q325 51 333 51 H415"/>
      <rect x="0" y="253" width="415" height="5" fill="var(--gold)"/>
    </svg>
    <div class="brand-name">HOLLAND'S</div>
    <h2 class="product-title">CUTTING BOARD FINISH</h2>
    <div class="tagline">All Natural Food-Safe Finish For All Types of Woodware</div>
    <div class="citrus-art" role="img" aria-label="Orange and lemon slices illustration"></div>
    <div class="honey-art" role="img" aria-label="Honeycomb cells illustration"></div>
    <div class="gold-band"></div>
    <div class="wood-drop-art" role="img" aria-label="Wood grain circle with oil drops illustration"></div>
    <div class="ingredients">Mineral oil, Beeswax, Carnauba wax, Orange oil and Lemon oil</div>
    <div class="volume">8 OZ.</div>
  </section>

</div>
</body>
</html>
```